Lien Post Card - (5.5 x 8.5)

FRONT OF POSTCARD
Is a Property Lien Putting Your Home at Risk?
HOA Liens • Tax Liens • Municipal Charges • Other Property-Related Liens
You may have options to resolve outstanding liens and protect your home.
A Refinance or Home Equity Line of Credit (HELOC) may help you:
✔ Pay off qualifying liens
✔ Consolidate debt into one manageable payment
✔ Access your home's equity
✔ Improve your financial flexibility
✔ Avoid additional penalties, fees, or collection actions
Don't wait until the situation becomes more difficult.
Call today for a confidential review of your options.
Bluegate Lending Partners, Inc.
(800) 647-2915 x 42
www.bluegatelendco.com
NMLS #381640
BACK OF POSTCARD
Your Home Equity Could Be the Solution
If you have received notices regarding:
• Delinquent Property Taxes
• HOA or Condo Association Assessments
• Municipal Utility Liens
• Special Assessments
• Other Property-Related Obligations
You may qualify for financing options designed to help satisfy those obligations and bring your property current.
Our experienced mortgage professionals can review your situation and discuss available programs, including:
• Cash-Out Refinancing
• Home Equity Lines of Credit (HELOCs)
• Home Equity Loans
• Debt Consolidation Solutions
Free Consultation • No Obligation
Contact Marcus Delaney today at (800) 647-2915 x42 or mdelaney@bluegatelendco.com (NMLS #57308)

```html
<!DOCTYPE html>
<html lang="en">
<head>
<meta charset="utf-8">
<title>Bluegate Lending Partners – Lien Postcard</title>
<link href="https://fonts.googleapis.com/css2?family=Poppins:wght@400;500;600;700;800&family=Noto+Serif:wght@700&display=swap" rel="stylesheet">
<style>
:root{
  --page:#dcdcdc;
  --label:#8a8a8a;
  --blue:#1a4b9c;
  --blue-mid:#2f63b4;
  --blue-light:#6596d6;
  --gold:#b8892a;
  --gold-light:#f6c06d;
  --ink:#1b1b1b;
  --white:#ffffff;
}
*{margin:0;padding:0;box-sizing:border-box}
html,body{width:953px;height:1200px;overflow:hidden}
body{background:var(--page);font-family:"Poppins",sans-serif;color:var(--ink);position:relative}
.side-label{position:absolute;left:90px;font-family:"Noto Serif",serif;font-weight:700;font-size:27px;color:var(--label);letter-spacing:1px}
.side-label.front{top:46px}
.side-label.back{top:1122px}
.card{position:absolute;left:92px;width:758px;height:490px;background:var(--white);overflow:hidden;box-shadow:4px 6px 10px rgba(0,0,0,.25)}
.card.front{top:89px}
.card.back{top:622px;left:91px}
.abs{position:absolute}
.brand{display:flex;align-items:center;gap:8px;font-weight:700;color:var(--blue);font-size:17px;line-height:1.15}
.brand-dot{width:22px;height:22px;border-radius:50%;background:var(--gold);flex:none}
/* front */
.front .brand{left:45px;top:62px;width:200px}
.headline{left:40px;top:152px;font-weight:800;font-size:30px;line-height:31px;color:var(--blue);letter-spacing:-.3px;text-transform:uppercase}
.gold{color:var(--gold)}
.lien-types{left:40px;top:253px;font-weight:500;font-size:12.3px;line-height:16px}
.lien-types span{margin-right:6px}
.offer-lead{left:40px;top:297px;font-weight:700;font-size:12.6px;line-height:15.5px;color:var(--blue)}
.benefits{left:40px;top:336px;list-style:none;font-size:12.6px;line-height:15.4px}
.benefits li{display:flex;align-items:center;gap:6px}
.benefits svg{flex:none}
.photo-svg{left:0;top:0}
.badge{left:395px;top:253px;width:136px;height:136px;border-radius:50%;background:linear-gradient(135deg,var(--blue) 0%,var(--blue-light) 100%);border:3px solid var(--gold-light);display:flex;align-items:center;justify-content:center}
.badge p{transform:rotate(10deg);color:var(--white);font-weight:600;font-size:12.2px;line-height:14px;text-align:center}
.call-bar{left:0;top:426px;width:390px;height:24px;background:var(--gold);clip-path:polygon(0 0,93% 0,100% 100%,0 100%);color:var(--white);font-weight:500;font-size:12px;line-height:24px;padding-left:40px}
.urge{left:405px;top:424px;font-weight:500;font-size:12px;color:var(--blue)}
.contact-bar{left:0;top:450px;width:758px;height:40px;background:linear-gradient(90deg,var(--blue) 0%,var(--blue-light) 100%);color:var(--white);display:flex;align-items:center}
.contact-bar .item{position:absolute;display:flex;align-items:center;gap:10px;font-weight:500;font-size:19px}
.contact-bar .phone{left:40px}
.contact-bar .web{left:272px}
.contact-bar .nmls{left:622px;font-size:14px;font-weight:400}
/* back */
.back-headline{left:45px;top:32px;font-weight:800;font-size:29px;line-height:31px;color:var(--blue)}
.couple-photo{left:342px;top:0;width:290px;height:110px;background:linear-gradient(90deg,rgba(255,255,255,0) 0%,#e7d6c2 25%,#c9a98a 60%,#e9e2d8 100%)}
.back .brand{left:612px;top:30px;width:135px;font-size:13px}
.back .brand-dot{width:16px;height:16px}
.notice-lead{left:45px;top:108px;font-weight:700;font-size:12.3px}
.notices{left:45px;top:139px;list-style:none;font-size:12.6px;line-height:15.4px}
.notices li::before{content:"•";color:var(--blue-light);margin-right:4px}
.qualify{left:45px;top:232px;width:350px;font-size:12.6px;line-height:15.2px}
.house-svg{left:0;top:300px}
.panel{left:413px;top:109px;width:345px;height:381px;background:linear-gradient(135deg,var(--blue) 0%,var(--blue-light) 100%);border-top-left-radius:40px;color:var(--white)}
.panel-intro{left:34px;top:25px;width:300px;font-size:12.6px;line-height:15.2px}
.programs{left:34px;top:86px;list-style:none;font-size:12.6px;line-height:15.4px}
.programs li::before{content:"•";margin-right:4px}
.tag{top:177px;height:28px;background:var(--gold-light);color:var(--blue);font-weight:600;font-size:13px;display:flex;align-items:center;gap:4px;justify-content:center}
.tag.consult{left:28px;width:157px}
.tag.obligation{left:190px;width:127px}
.contact-title{left:31px;top:242px;font-weight:700;font-size:19px}
.rep-name{left:31px;top:279px;font-weight:600;font-size:12.5px;color:var(--gold-light)}
.rep-line{left:31px;display:flex;align-items:center;gap:6px;font-size:12px;white-space:nowrap;z-index:2}
.rep-phone{top:296px}
.rep-email{top:317px}
.rep-nmls{left:31px;top:350px;font-size:7.5px}
.portrait{left:240px;top:210px;width:105px;height:171px;z-index:1;background:linear-gradient(180deg,#3a4f7d 0%,#2a2a2f 60%,#151517 100%)}
</style>
</head>
<body>
<div class="side-label front">FRONT</div>

<section class="card front">
  <svg class="abs photo-svg" width="758" height="490" viewBox="0 0 758 490" role="img" aria-label="Photo of a worried couple reviewing bills at home">
    <defs>
      <linearGradient id="coupleTone" x1="0" y1="0" x2="1" y2="1">
        <stop offset="0" stop-color="#d9d6d2"/>
        <stop offset=".5" stop-color="#6f7f98"/>
        <stop offset="1" stop-color="#b9a48f"/>
      </linearGradient>
    </defs>
    <path d="M477,0 C440,45 420,125 435,205 C455,305 550,385 660,380 C705,378 740,368 758,357 L758,0 Z" fill="url(#coupleTone)"/>
    <path d="M467,0 C428,45 408,125 424,205 C444,310 545,393 660,390 C705,389 740,378 758,368" fill="none" stroke="var(--gold-light)" stroke-width="4"/>
    <path d="M455,0 C415,45 396,125 412,205 C432,318 540,402 660,400 C705,399 740,388 758,378" fill="none" stroke="var(--blue)" stroke-width="3"/>
  </svg>

  <div class="abs brand"><span class="brand-dot"></span>Bluegate Lending Partners</div>

  <h1 class="abs headline">Is a Property Loan<br>Putting <span class="gold">Your Home</span><br>at Risk?</h1>

  <p class="abs lien-types"><span>• HOA Liens</span> <span>• Tax Liens</span> <span>• Municipal Charges</span><br>• Other Property-Related Liens</p>

  <p class="abs offer-lead">A Refinance or Home Equity Line of Credit (HELOC)<br>may help you:</p>

  <ul class="abs benefits">
    <li><svg width="10" height="8" viewBox="0 0 10 8"><path d="M1,4 L4,7 L9,1" fill="none" stroke="var(--blue-light)" stroke-width="2"/></svg>Pay off qualifying liens</li>
    <li><svg width="10" height="8" viewBox="0 0 10 8"><path d="M1,4 L4,7 L9,1" fill="none" stroke="var(--blue-light)" stroke-width="2"/></svg>Consolidate debt into one manageable payment</li>
    <li><svg width="10" height="8" viewBox="0 0 10 8"><path d="M1,4 L4,7 L9,1" fill="none" stroke="var(--blue-light)" stroke-width="2"/></svg>Access your home's equity</li>
    <li><svg width="10" height="8" viewBox="0 0 10 8"><path d="M1,4 L4,7 L9,1" fill="none" stroke="var(--blue-light)" stroke-width="2"/></svg>Improve your financial flexibility</li>
    <li><svg width="10" height="8" viewBox="0 0 10 8"><path d="M1,4 L4,7 L9,1" fill="none" stroke="var(--blue-light)" stroke-width="2"/></svg>Avoid additional penalties, fees, or collection actions</li>
  </ul>

  <div class="abs badge"><p>You may<br>have options<br>to resolve<br>outstanding liens<br>and protect your<br>home.</p></div>

  <div class="abs call-bar">Call today for a confidential review of your options.</div>
  <p class="abs urge">Don't wait until the situation becomes more difficult.</p>

  <div class="abs contact-bar">
    <span class="item phone"><svg width="14" height="14" viewBox="0 0 24 24"><path d="M6.6 10.8a15 15 0 0 0 6.6 6.6l2.2-2.2c.3-.3.7-.4 1-.2 1.1.4 2.3.6 3.6.6.6 0 1 .4 1 1V20c0 .6-.4 1-1 1A17 17 0 0 1 3 4c0-.6.4-1 1-1h3.5c.6 0 1 .4 1 1 0 1.3.2 2.5.6 3.6.1.3 0 .7-.2 1z" fill="var(--gold-light)"/></svg>(800) 647-2915 x 42</span>
    <span class="item web"><svg width="14" height="14" viewBox="0 0 24 24" fill="none" stroke="var(--gold-light)" stroke-width="2"><circle cx="12" cy="12" r="10"/><path d="M2 12h20M12 2c3 3 3 17 0 20M12 2c-3 3-3 17 0 20"/></svg>www.bluegatelendco.com</span>
    <span class="item nmls">NMLS #381640</span>
  </div>
</section>

<section class="card back">
  <div class="abs couple-photo" role="img" aria-label="Photo of a smiling couple holding a tape measure frame among moving boxes"></div>
  <div class="abs brand"><span class="brand-dot"></span>Bluegate Lending Partners</div>

  <h2 class="abs back-headline">Your Home Equity<br>Could Be <span class="gold">the Solution</span></h2>

  <p class="abs notice-lead">If you have received notices regarding:</p>
  <ul class="abs notices">
    <li>Delinquent Property Taxes</li>
    <li>HOA or Condo Association Assessments</li>
    <li>Municipal Utility Liens</li>
    <li>Special Assessments</li>
    <li>Other Property-Related Obligations</li>
  </ul>
  <p class="abs qualify">You may qualify for financing options designed to help satisfy those obligations and bring your property current.</p>

  <svg class="abs house-svg" width="420" height="190" viewBox="0 0 420 190" role="img" aria-label="Black and white photo of a two-storey house in winter">
    <defs>
      <linearGradient id="houseTone" x1="0" y1="0" x2="1" y2="1">
        <stop offset="0" stop-color="#bdbdbd"/>
        <stop offset=".6" stop-color="#4d4d4d"/>
        <stop offset="1" stop-color="#2a2a2a"/>
      </linearGradient>
    </defs>
    <path d="M0,92 C80,35 190,20 270,48 C345,78 390,130 402,190 L0,190 Z" fill="url(#houseTone)"/>
    <path d="M0,82 C80,24 195,8 276,38 C352,68 398,125 412,190" fill="none" stroke="var(--gold-light)" stroke-width="4"/>
    <path d="M0,71 C80,12 200,-4 282,27 C360,58 408,120 420,190" fill="none" stroke="var(--blue)" stroke-width="3"/>
  </svg>

  <div class="abs panel">
    <p class="abs panel-intro">Our experienced mortgage professionals can review your situation and discuss available programs, including:</p>
    <ul class="abs programs">
      <li>Cash-Out Refinancing</li>
      <li>Home Equity Lines of Credit (HELOCs)</li>
      <li>Home Equity Loans</li>
      <li>Debt Consolidation Solutions</li>
    </ul>
    <div class="abs tag consult"><svg width="14" height="14" viewBox="0 0 24 24" fill="none" stroke="var(--blue)" stroke-width="2.4"><path d="M4 15v-3a8 8 0 0 1 16 0v3"/><rect x="3" y="14" width="4" height="6" rx="1"/><rect x="17" y="14" width="4" height="6" rx="1"/></svg>Free Consultation</div>
    <div class="abs tag obligation"><svg width="14" height="14" viewBox="0 0 24 24" fill="none" stroke="var(--blue)" stroke-width="2.4"><circle cx="12" cy="12" r="9"/><path d="M6 6l12 12"/></svg>No Obligation</div>

    <div class="abs portrait" role="img" aria-label="Portrait of the loan officer in a hat and dark jacket"></div>

    <h3 class="abs contact-title">Contact</h3>
    <p class="abs rep-name">Marcus Delaney</p>
    <p class="abs rep-line rep-phone"><svg width="12" height="12" viewBox="0 0 24 24"><path d="M6.6 10.8a15 15 0 0 0 6.6 6.6l2.2-2.2c.3-.3.7-.4 1-.2 1.1.4 2.3.6 3.6.6.6 0 1 .4 1 1V20c0 .6-.4 1-1 1A17 17 0 0 1 3 4c0-.6.4-1 1-1h3.5c.6 0 1 .4 1 1 0 1.3.2 2.5.6 3.6.1.3 0 .7-.2 1z" fill="var(--gold-light)"/></svg>(800) 647-2915 x42</p>
    <p class="abs rep-line rep-email"><svg width="12" height="12" viewBox="0 0 24 24" fill="none" stroke="var(--gold-light)" stroke-width="2.4"><rect x="2" y="5" width="20" height="14" rx="1"/><path d="M2 6l10 7 10-7"/></svg>mdelaney@bluegatelendco.com</p>
    <p class="abs rep-nmls">(NMLS #57308)</p>
  </div>
</section>

<div class="side-label back">BACK</div>
</body>
</html>
```